Construction company stationary design

We're wanting to develop a new professional stationary set for a newly establised property related business using our existing logo (attached). Business incorporates renovations, property investment and property development.

Specifically needing letter head, business cards, envelopes, email signature and need to get tshirt and caps embroydered.

Looking for something quite modern but professional using white, black and green.

Investment

```html
<!DOCTYPE html>
<html lang="en">
<head>
<meta charset="utf-8">
<title>RKV Builders – Stationery Set</title>
<link href="https://fonts.googleapis.com/css2?family=Jost:wght@400;500;700&display=swap" rel="stylesheet">
<style>
  :root{
    --green:#7dc242;
    --black:#111111;
    --white:#ffffff;
    --paper:#fbfbfb;
    --ink:#444444;
    --muted:#8a8a8a;
    --backdrop:#c48a55;
    --font:"Jost", Arial, sans-serif;
  }
  *{box-sizing:border-box;margin:0;padding:0}
  html,body{width:1200px;height:581px;overflow:hidden}
  body{background:var(--backdrop);font-family:var(--font);color:var(--ink);position:relative}
  .item{position:absolute}
  .sheet{background:var(--paper);box-shadow:0 1px 3px rgba(0,0,0,.25)}
  .brand{display:flex;flex-direction:column;align-items:center;color:var(--green);font-weight:700;line-height:1}
  .brand .name{font-size:22px;letter-spacing:.5px}
  .brand .tag{font-size:6px;letter-spacing:1.2px;margin-top:2px}
  .brand.white{color:var(--white)}
  .sheet .brand{position:absolute;top:12px;left:50%;transform:translateX(-50%)}
  .sheet-2 .brand,.sheet-3 .brand{left:14px;transform:none;align-items:flex-start}
  .contact{position:absolute;top:18px;right:8px;font-size:5px;line-height:7.5px;color:var(--ink)}
  .contact span::before,.card-info .line::before{content:"";display:inline-block;width:4px;height:4px;border-radius:50%;background:var(--green);margin-right:3px;vertical-align:middle}
  .contact .addr::before,.card-info .addr::before{display:none}
  .sheet-foot{position:absolute;bottom:7px;left:0;right:0;text-align:center;font-size:5px;color:var(--ink);letter-spacing:.3px}
  .sheet-foot.wide{letter-spacing:2px}
  .fax-title{position:absolute;top:74px;left:14px;font-size:16px;color:var(--black);font-weight:400}
  .fax-grid{position:absolute;top:101px;left:14px;width:229px;display:grid;grid-template-columns:1.4fr 1fr;column-gap:0;row-gap:7px;font-size:4.5px}
  .fax-grid div{border-bottom:.7px solid var(--ink);padding-bottom:1px}
  .fax-checks{position:absolute;top:164px;left:14px;display:flex;gap:8px;font-size:4.5px}
  .fax-checks span::before{content:"";display:inline-block;width:5px;height:5px;border:.7px solid var(--ink);margin-right:3px;vertical-align:middle}
  .label{position:absolute;color:var(--white);font-size:18px;font-weight:400}
  .env{background:var(--white);box-shadow:0 1px 3px rgba(0,0,0,.25);overflow:hidden}
  .env .flap{position:absolute;inset:0}
  .env .brand{position:absolute}
  .env-front .brand{left:18px;top:36px;align-items:flex-start}
  .env-front .addr{position:absolute;left:18px;top:80px;font-size:4.5px}
  .env-front .web{position:absolute;left:18px;bottom:6px;font-size:5px;letter-spacing:1.5px}
  .card{display:flex;align-items:center;box-shadow:0 1px 3px rgba(0,0,0,.3);overflow:hidden}
  .card.light{background:var(--white)}
  .card.dark{background:var(--black)}
  .card.accent{background:var(--green)}
  .card .logo-side{flex:1.3;display:flex;justify-content:center}
  .card-info{flex:1;border-left:.6px solid #bbb;padding-left:5px;font-size:4.6px;line-height:6.5px;color:var(--ink)}
  .card.dark .card-info{color:#ddd;border-color:#555}
  .card-info .person{color:var(--green);font-weight:700;font-size:5.5px;margin-bottom:2px}
  .card-info .addr{margin-top:3px}
  .card.center{flex-direction:column;justify-content:center}
  .card.center .brand .name{font-size:28px}
  .card.center .brand .tag{font-size:7px}
  .card .web{font-size:5px;letter-spacing:1.5px;margin-top:9px;color:var(--white)}
  .card.dark .web{color:#bbb}
  .sig .brand .name{font-size:24px}
  .sig .card-info{font-size:5px;line-height:7px}
  .shirt{background:var(--white);display:flex;flex-direction:column;align-items:center;box-shadow:0 1px 3px rgba(0,0,0,.25)}
  .shirt .collar{width:60px;height:8px;background:var(--green);border-radius:0 0 30px 30px;margin-top:10px}
  .shirt .brand{margin-top:42px}
  .shirt .brand .name{font-size:12px}
  .shirt .brand .tag{font-size:3.5px}
  .cap{background:var(--black);display:flex;justify-content:center;align-items:center}
  .cap-front{border-radius:90px 90px 14px 14px}
  .cap-front .brand .name{font-size:30px}
  .cap-front .brand .tag{font-size:8px}
  .cap-back{border-radius:110px 110px 20px 20px}
  .cap-back .button{position:absolute;top:-4px;left:50%;width:14px;height:7px;background:var(--green);border-radius:7px 7px 0 0;transform:translateX(-50%)}
  .cap-front .button{position:absolute;top:-4px;left:50%;width:14px;height:7px;background:var(--green);border-radius:7px 7px 0 0;transform:translateX(-50%)}
  .cap-back .mark{width:18px;height:18px;background:var(--green)}
  .strap{position:absolute;bottom:18px;left:50%;transform:translateX(-50%);width:40px;height:10px;border:2px solid #333;border-radius:2px}
</style>
</head>
<body>

  <!-- Letterhead option 1 -->
  <section class="item sheet sheet-1" style="left:9px;top:3px;width:255px;height:329px">
    <div class="brand"><span class="name">RKV</span><span class="tag">BUILDERS</span></div>
    <p class="sheet-foot">12, Harbour Court, Lakeside, State 0150 &nbsp;|&nbsp; 0123 456780 &nbsp;|&nbsp; info@rkvbuild.com &nbsp;|&nbsp; www.rkvbuild.com</p>
  </section>
  <p class="label" style="left:92px;top:341px">Option-1</p>

  <!-- Letterhead option 2 -->
  <section class="item sheet sheet-2" style="left:289px;top:3px;width:255px;height:329px">
    <div class="brand"><span class="name">RKV</span><span class="tag">BUILDERS</span></div>
    <div class="contact">
      <span>0123 456780</span><br><span>info@rkvbuild.com</span><br>
      <span class="addr">12, Harbour Court,<br>Lakeside, State 0150</span>
    </div>
    <p class="sheet-foot wide">www.rkvbuild.com</p>
  </section>
  <p class="label" style="left:372px;top:341px">Option-2</p>

  <!-- Letterhead option 3 (fax) -->
  <section class="item sheet sheet-3" style="left:573px;top:3px;width:255px;height:329px">
    <div class="brand"><span class="name">RKV</span><span class="tag">BUILDERS</span></div>
    <div class="contact">
      <span>0123 456780</span><br><span>info@rkvbuild.com</span><br><span>www.rkvbuild.com</span>
    </div>
    <h2 class="fax-title">FAX</h2>
    <div class="fax-grid">
      <div>To :</div><div>From :</div>
      <div>Fax :</div><div>Pages :</div>
      <div>Phone :</div><div>Date :</div>
      <div>Re :</div><div>CC :</div>
    </div>
    <div class="fax-checks">
      <span>Urgent</span><span>For Review</span><span>Please Comment</span><span>Please Reply</span><span>Please Recycle</span>
    </div>
    <p class="sheet-foot">12, Harbour Court, Lakeside, State 0150</p>
  </section>
  <p class="label" style="left:655px;top:341px">Option-3</p>

  <!-- Envelopes -->
  <section class="item env env-back" style="left:892px;top:20px;width:278px;height:128px">
    <svg class="flap" viewBox="0 0 278 128" preserveAspectRatio="none"><path d="M0 0H278V12L170 52Q139 62 108 52L0 12Z" fill="var(--black)"/></svg>
    <div class="brand" style="left:112px;top:20px"><span class="name" style="font-size:16px">RKV</span></div>
  </section>
  <section class="item env env-mid" style="left:847px;top:75px;width:285px;height:121px">
    <svg class="flap" viewBox="0 0 285 121" preserveAspectRatio="none"><path d="M0 0H285V8L170 52Q142 60 115 52L0 8" fill="none" stroke="var(--black)" stroke-width="1"/></svg>
    <div class="brand" style="left:120px;top:20px"><span class="name" style="font-size:16px">RKV</span></div>
  </section>
  <section class="item env env-front" style="left:877px;top:132px;width:285px;height:128px">
    <div class="brand"><span class="name">RKV</span><span class="tag">BUILDERS</span></div>
    <p class="addr">12, Harbour Court, Lakeside, State 0150</p>
    <p class="web">www.rkvbuild.com</p>
  </section>

  <!-- Business cards -->
  <section class="item card light" style="left:858px;top:278px;width:152px;height:86px">
    <div class="logo-side"><div class="brand"><span class="name">RKV</span><span class="tag">BUILDERS</span></div></div>
    <div class="card-info">
      <p class="person">PERSONS NAME</p>
      <p class="line">0123 456780</p><p class="line">0123 456781</p>
      <p class="line">info@rkvbuild.com</p><p class="line">www.rkvbuild.com</p>
      <p class="addr">12, Harbour Court,<br>Lakeside, State 0150</p>
    </div>
  </section>
  <section class="item card accent center" style="left:1025px;top:278px;width:151px;height:86px">
    <div class="brand white"><span class="name">RKV</span><span class="tag">BUILDERS</span></div>
    <p class="web">www.rkvbuild.com</p>
  </section>
  <section class="item card dark" style="left:858px;top:373px;width:152px;height:86px">
    <div class="logo-side"><div class="brand"><span class="name">RKV</span><span class="tag">BUILDERS</span></div></div>
    <div class="card-info">
      <p class="person">PERSONS NAME</p>
      <p class="line">0123 456780</p><p class="line">0123 456781</p>
      <p class="line">info@rkvbuild.com</p><p class="line">www.rkvbuild.com</p>
      <p class="addr">12, Harbour Court,<br>Lakeside, State 0150</p>
    </div>
  </section>
  <section class="item card dark center" style="left:1025px;top:373px;width:151px;height:86px">
    <div class="brand"><span class="name">RKV</span><span class="tag">BUILDERS</span></div>
    <p class="web">www.rkvbuild.com</p>
  </section>

  <!-- Email signatures -->
  <section class="item card light sig" style="left:818px;top:478px;width:180px;height:80px">
    <div class="logo-side"><div class="brand"><span class="name">RKV</span><span class="tag">BUILDERS</span></div></div>
    <div class="card-info">
      <p class="person">PERSONS NAME</p>
      <p class="line">0123 456780</p><p class="line">0123 456781</p>
      <p class="line">info@rkvbuild.com</p><p class="line">www.rkvbuild.com</p>
      <p class="addr">12, Harbour Court,<br>Lakeside, State 0150</p>
    </div>
  </section>
  <p class="label" style="left:890px;top:562px;font-size:13px">E.S - 1</p>
  <section class="item card dark sig" style="left:1007px;top:478px;width:180px;height:80px">
    <div class="logo-side"><div class="brand"><span class="name">RKV</span><span class="tag">BUILDERS</span></div></div>
    <div class="card-info">
      <p class="person">PERSONS NAME</p>
      <p class="line">0123 456780</p><p class="line">0123 456781</p>
      <p class="line">info@rkvbuild.com</p><p class="line">www.rkvbuild.com</p>
      <p class="addr">12, Harbour Court,<br>Lakeside, State 0150</p>
    </div>
  </section>
  <p class="label" style="left:1079px;top:562px;font-size:13px">E.S - 2</p>

  <!-- Apparel -->
  <section class="item shirt" style="left:130px;top:380px;width:148px;height:196px" aria-label="White T-shirt with green collar and chest print">
    <div class="collar"></div>
    <div class="brand"><span class="name">RKV</span><span class="tag">BUILDERS</span></div>
  </section>
  <section class="item cap cap-front" style="left:318px;top:440px;width:190px;height:118px" aria-label="Black cap, front embroidery">
    <span class="button"></span>
    <div class="brand"><span class="name">RKV</span><span class="tag">BUILDERS</span></div>
  </section>
  <section class="item cap cap-back" style="left:540px;top:440px;width:220px;height:118px" aria-label="Black cap, back embroidery">
    <span class="button"></span>
    <span class="mark"></span>
    <span class="strap"></span>
  </section>

</body>
</html>
```